Brochure Design Project (Design Studio)

Items required:
1-Brochure. We suggest 15Cm X 15 Cm after cutting.
2-Business Card.
3-Head letter.
4-Folder ( folder should carry the Brochure in pocket and the business card in a pocket on the opposite side of the folder.
5-Envelope to carry everything.
This brochure is expected to draw attention of high level management in companies to the quality and creativity of the design work and encourage them to do business with us. note that brochure will be printed in high quality printing and paper.
The game plan is as follows:
Over all description, the theme of the brochure is drawn from the website theme (website will be uploaded shortly, pictures of the website are attached, logo appears in the top left corner). Please avoid direct copying from the website unless it is a creative copying, just draw the theme from there. however, we need it to be elegant, stylish and class in colors and style. This is a MUST.
Furthermore, the main items of the Brochure:
1-The Studio is not just a studio: we will take about how Branding. A file is attached of the content. (slight changes/modification can apply during the designing process)
2-The Process: this one has to be a visual illustration of the process, it has to be very creative, could be elegant arrows and comics, could be elegant drawing, could be an elegant icons. The drawing should be separate from the steps, we need to the drawing and we need to have the steps listed and commentary, or if want to integrate both in one in an artistic way. Just don’t lose track of the theme and elegance. (steps and commentary are attached, slight changes/modification can apply at anytime.
3-Our Team: another drawing of your suggestion to illustrate the team members, we need to include the names and designation as well leave a place for some of them to say what they need to say about their style of designing. I leave it for your imagination to put this all together in a nice attractive visual illustration.
4-Works: this section will generally show the works of our designers. It needs to be focused on the works themselves, client should be able to view the details of the works ( note that when it comes to brochures and websites, we don’t need to reach to the extent with which the client can read the text in those pictures of the website or brochure, but still can see the overall design clearly). Each design is to carry the name of the designer. Last thing, this section will classify works into categories, like, Brochures, Corporate identity, print design. We didn’t finalize those categories, we will provide them to you shortly, last thing to be said, we are planning to include around 25-30 designs of each sub-category, eg. Corporate identity will have 30 business card s designs and 30 stationary designs.
5-Contacts: the company contacts.
We the brochure after printing should be 15x15 Cm.
Creativity and art work is a major player in selection.
general managers, owners
Printing

```html
<!DOCTYPE html>
<html lang="en">
<head>
<meta charset="utf-8">
<title>Corvane Studio – Brochure Spread</title>
<link rel="stylesheet" href="https://fonts.googleapis.com/css2?family=Jost:wght@400;500&family=Oswald:wght@500&display=swap">
<style>
  :root {
    --stage: #f1f1f1;
    --sheet: #ffffff;
    --page-grey: #9da09b;
    --page-edge: #8e918c;
    --band: #ffffff;
    --ink-white: #ffffff;
    --lime: #d9f55e;
    --crimson: #b3002b;
    --ribbon-light: #b13a3a;
    --ribbon-dark: #5e1414;
    --brand-ink: #4a5560;
    --brand-accent: #9cc23a;
    --portrait-light: #eef07a;
    --portrait-dark: #c9cf6a;
  }
  * { box-sizing: border-box; margin: 0; padding: 0; }
  html, body { width: 1200px; height: 634px; overflow: hidden; }
  body {
    background: var(--stage);
    font-family: "Jost", "Futura", sans-serif;
    position: relative;
  }
  .spread {
    position: absolute; left: 62px; top: 42px; width: 1074px; height: 546px;
    background: var(--sheet);
    box-shadow: 0 6px 18px rgba(0,0,0,.22);
  }
  .page {
    position: absolute; top: 66px; width: 504px; height: 502px;
    background: var(--page-grey);
    border-top: 8px solid var(--page-edge);
    color: var(--ink-white);
  }
  .page--process { left: 70px; }
  .page--team { left: 628px; }
  .page__band {
    position: absolute; left: 0; top: 0; width: 100%; height: 56px;
    background: var(--band);
  }
  .brand {
    position: absolute; right: 20px; top: 12px;
    display: flex; align-items: center; gap: 10px;
    color: var(--brand-ink); font-weight: 400;
  }
  .brand__name { font-size: 25px; letter-spacing: .5px; }
  .brand__rule { width: 2px; height: 22px; background: var(--brand-accent); }
  .brand__tag { font-size: 13px; letter-spacing: 2.5px; text-transform: uppercase; }
  .ribbon {
    position: absolute; left: 12px; top: 10px; width: 118px; height: 36px;
    transform: rotate(-14deg);
    background: linear-gradient(180deg, var(--ribbon-light), var(--ribbon-dark));
    border-radius: 4px;
    box-shadow: 2px 3px 4px rgba(0,0,0,.35);
    color: var(--ink-white); font-size: 17px;
    display: flex; align-items: center; justify-content: center;
  }
  .phase { position: absolute; width: 222px; font-size: 11.3px; line-height: 15.4px; }
  .phase__icon { position: absolute; left: -18px; top: -38px; width: 38px; height: 36px; }
  .phase__step { color: var(--lime); font-size: 14px; line-height: 16px; }
  .phase__title { color: var(--crimson); font-size: 14px; line-height: 16px; }
  .team-copy {
    position: absolute; width: 232px; font-size: 11.3px; line-height: 15.4px;
  }
  .team-heading {
    position: absolute; left: 18px; top: 246px;
    font-family: "Oswald", "Arial Narrow", sans-serif; font-weight: 500;
    font-size: 24px; color: var(--crimson);
  }
  .member { position: absolute; top: 292px; width: 100px; text-align: center; }
  .member__portrait {
    display: block; width: 100px; height: 120px;
    background: linear-gradient(150deg, var(--portrait-light), var(--portrait-dark));
    border: 2px solid #fff;
  }
  .member__name { color: var(--lime); font-size: 11px; margin-top: 4px; }
  .member__role { color: var(--lime); font-size: 9.5px; line-height: 11px; }
</style>
</head>
<body>
<svg width="0" height="0" style="position:absolute">
  <defs>
    <linearGradient id="arrowFill" x1="0" y1="0" x2="0" y2="1">
      <stop offset="0" stop-color="#7a5a5a"/>
      <stop offset="1" stop-color="#3a2a2a"/>
    </linearGradient>
    <symbol id="curved-arrow" viewBox="0 0 38 36">
      <path d="M6 32 C4 18 12 9 24 9 L24 3 L36 13 L24 23 L24 17 C16 17 10 22 6 32 Z" fill="url(#arrowFill)" stroke="#fff" stroke-width="1"/>
    </symbol>
  </defs>
</svg>

<div class="spread"></div>

<section class="page page--process">
  <header class="page__band">
    <div class="ribbon">Brainstorming!</div>
    <div class="brand"><span class="brand__name">Corvane Studio</span><span class="brand__rule"></span><span class="brand__tag">Crafted Designs</span></div>
  </header>

  <article class="phase" style="left:27px; top:118px;">
    <svg class="phase__icon"><use href="#curved-arrow"/></svg>
    <p><span class="phase__step">Phase one: </span><span class="phase__title">Brainstorming:</span></p>
    <p>We identify the objectives of the design. We aim to identify the ultimate perception to be made among customers. We as well tap on the challenges faced by our customers including competitive force.<br>We don’t compromise on understanding the client requirements at a core level in order to see the mission of creating any particular design from the client’s eyes not ours!</p>
  </article>

  <article class="phase" style="left:27px; top:348px;">
    <svg class="phase__icon"><use href="#curved-arrow"/></svg>
    <p class="phase__step">Phase two:</p>
    <p class="phase__title">Build technical Description.</p>
    <p>Creative Manager builds a technical description of client’s requirements which translates the requirements to designing language. And then the job is dispatched to designers.</p>
  </article>

  <article class="phase" style="left:286px; top:92px; width:205px;">
    <svg class="phase__icon"><use href="#curved-arrow"/></svg>
    <p class="phase__step">Phase three:</p>
    <p class="phase__title">Produce many concept design.</p>
    <p>Each designer produces visual composition based on his understanding of the requirements. Clients expect 5-10 different ideas for their requirements according to different styles of designing.<br>Our business concept guarantees the maximum level of creativity in generating ideas.</p>
  </article>

  <article class="phase" style="left:286px; top:292px; width:205px;">
    <svg class="phase__icon"><use href="#curved-arrow"/></svg>
    <p class="phase__step">Phase four:</p>
    <p class="phase__title">Selection and implementation:</p>
    <p>All Concept mockups are passed to client to select best one. The selected design is revised several times with client till client is ultimately satisfied with the results.</p>
  </article>

  <article class="phase" style="left:286px; top:428px; width:205px;">
    <svg class="phase__icon"><use href="#curved-arrow"/></svg>
    <p><span class="phase__step">Phase five:</span><span class="phase__title">Execution:</span></p>
    <p>Final design is sent for printing and execution.</p>
  </article>
</section>

<section class="page page--team">
  <header class="page__band">
    <div class="ribbon">Our Team!</div>
    <div class="brand"><span class="brand__name">Corvane Studio</span><span class="brand__rule"></span><span class="brand__tag">Crafted Designs</span></div>
  </header>

  <p class="team-copy" style="left:19px; top:82px;">Our team of designer is a multinational team, not only their passports differ but as well their style of designing which provides the highest level of creativity to provide you with lots of fresh and unique ideas.<br>Our creative manager is an artist who has a strong eye for details and enjoys a natural talent in building art. Just like a musician can recognize the right tone, our</p>
  <p class="team-copy" style="left:260px; top:82px;">creative manager can dress up your business with the best visual composition.<br>Our business development team has on board individuals with strong business sense and long experience in building brands. They understand the common challenges in front of your business progression and have the skills and talents to tap on the hidden ones. They will definitely help you achieve your objectives.</p>

  <h2 class="team-heading">Our creative team:</h2>

  <figure class="member" style="left:22px;">
    <span class="member__portrait" role="img" aria-label="Illustrated portrait of the creative manager"></span>
    <figcaption><p class="member__name">Mira Castell</p><p class="member__role">Creative Manager</p></figcaption>
  </figure>
  <figure class="member" style="left:204px;">
    <span class="member__portrait" role="img" aria-label="Illustrated portrait of the creative manager"></span>
    <figcaption><p class="member__name">Mira Castell</p><p class="member__role">Creative Manager</p></figcaption>
  </figure>
  <figure class="member" style="left:382px;">
    <span class="member__portrait" role="img" aria-label="Illustrated portrait of the creative manager"></span>
    <figcaption><p class="member__name">Mira Castell</p><p class="member__role">Creative Manager</p></figcaption>
  </figure>
</section>
</body>
</html>
```